Need a cover for eBook:
Title is: 41 Blunders That Sink Your Indie-Released Volume.
Remarks about the title: I know that is difficult to design a cover with a number. You can add the word TOP (in caps or not) before 41 blunders. It is not mandatory to insert the word TOP. It is up to you if you think you can create a better cover.
Subtitle is: A Newcomer's Manual for Releasing Solo, Arranging Pictures and Words, Planning Pages, Boosting Sign-ups and Moving More Copies
Author: Dennis R. Walbrey
Publisher: Quillmark Press
The book made the presentation of errors that can occur during the production of an ebook. Title must be big, the title should be readable even when the image is reduced in size. No photo please.
I join my projects as an example. Do what you want but I need impact.

Target Market(s)

Book to sell first at Brimfold Reader Shop. Target is authors, men or women, who want to produce ebooks.

Industry/Entity Type

Publishing Company

Font styles to use
Sans Serif

Colors
3176b5
9bcb3c

Requirements
Must have
• High readability when cover is small.
• Here is the definition of the word KILL
• put an end to or cause the failure or defeat of (something).
• "the committee voted to kill the project"
• synonyms: destroy, put an end to, end, extinguish, dash, quash, ruin, wreck, shatter, smash, crush, scotch, thwart; informalput the kibosh on, stymie, scuttle
• "this would kill all hopes of progress"
• veto, defeat, vote down, rule against, reject, throw out, overrule, overturn, put a stop to, quash, squash
• "an opposition attempt to kill the bill"
Nice to have
• I suggested 2 colors but you can you use another one or two. I want cover that sell. There is so bright ideas here. Come on down!
Should not have
• No picture or photo. If a photo or an object had power to the cover, you can insert one. I don't want a photo-collage.

```html
<!DOCTYPE html>
<html lang="en">
<head>
<meta charset="utf-8">
<title>41 Blunders That Sink Your Indie-Released Volume — Cover</title>
<link rel="stylesheet" href="https://fonts.googleapis.com/css2?family=Bowlby+One&family=Anton&family=Roboto+Condensed:wght@700;900&family=Libre+Baskerville:wght@700&display=swap">
<style>
  :root {
    --cover-green: #9bcb3c;
    --brand-blue: #3176b5;
    --blue-light: #5d9ad6;
    --blue-dark: #1d4f82;
    --outline-navy: #0c2440;
    --burst-red: #e8243a;
    --ink: #0b0b0b;
    --paper: #ffffff;
    --burst-green: #9bcb3c;
  }
  html, body {
    margin: 0;
    padding: 0;
    overflow: hidden;
    background: var(--cover-green);
  }
  .cover {
    position: relative;
    width: 927px;
    height: 1200px;
    background: var(--cover-green);
    overflow: hidden;
  }
  .cover-art {
    position: absolute;
    inset: 0;
    width: 927px;
    height: 1200px;
  }
  .hero-number, .hero-word {
    fill: url(#bevel-blue);
    stroke: var(--outline-navy);
    stroke-width: 4;
    paint-order: stroke fill;
    filter: url(#hero-shadow);
  }
  .hero-number {
    font-family: "Bowlby One", "Arial Black", sans-serif;
    font-size: 250px;
  }
  .hero-word {
    font-family: "Anton", "Impact", sans-serif;
    font-size: 150px;
  }
  .burst {
    fill: var(--brand-blue);
    stroke: var(--burst-red);
    stroke-width: 3;
    stroke-linejoin: miter;
  }
  .burst-small, .burst-big {
    font-family: "Libre Baskerville", Georgia, serif;
    font-weight: 700;
    text-anchor: middle;
  }
  .burst-small { fill: var(--ink); font-size: 25px; }
  .burst-big { fill: var(--burst-green); font-size: 46px; }

  .title-rest {
    position: absolute;
    top: 412px;
    left: 0;
    width: 927px;
    margin: 0;
    text-align: center;
    font-family: "Roboto Condensed", "Arial Narrow", sans-serif;
    font-weight: 900;
    font-size: 60px;
    line-height: 64px;
    color: var(--ink);
    letter-spacing: -0.5px;
    text-shadow:
      2px 0 0 var(--paper), -2px 0 0 var(--paper),
      0 2px 0 var(--paper), 0 -2px 0 var(--paper),
      2px 2px 0 var(--paper), -2px -2px 0 var(--paper),
      2px -2px 0 var(--paper), -2px 2px 0 var(--paper);
  }
  .subtitle {
    position: absolute;
    top: 780px;
    left: 101px;
    width: 380px;
    margin: 0;
    font-family: "Libre Baskerville", Georgia, serif;
    font-weight: 700;
    font-size: 24px;
    line-height: 43px;
    color: var(--ink);
  }
  .author, .publisher {
    position: absolute;
    top: 1090px;
    margin: 0;
    font-family: "Roboto Condensed", "Arial Narrow", sans-serif;
    font-weight: 700;
    font-size: 32px;
    color: var(--ink);
  }
  .author { left: 72px; }
  .publisher { right: 64px; }
</style>
</head>
<body>
<main class="cover">
  <svg class="cover-art" viewBox="0 0 927 1200" aria-hidden="false">
    <defs>
      <linearGradient id="bevel-blue" x1="0" y1="0" x2="0" y2="1">
        <stop offset="0" stop-color="var(--blue-light)"/>
        <stop offset="0.5" stop-color="var(--brand-blue)"/>
        <stop offset="1" stop-color="var(--blue-dark)"/>
      </linearGradient>
      <filter id="hero-shadow" x="-10%" y="-10%" width="120%" height="130%">
        <feDropShadow dx="4" dy="5" stdDeviation="4" flood-color="#1a3300" flood-opacity="0.45"/>
      </filter>
    </defs>

    <text class="hero-number" x="463" y="232" text-anchor="middle" textLength="470" lengthAdjust="spacingAndGlyphs">41</text>
    <text class="hero-word" x="470" y="388" text-anchor="middle" textLength="575" lengthAdjust="spacingAndGlyphs">Blunders</text>

    <polygon class="burst" points="660,718 692,796 765,741 748,822 842,806 781,867 870,893 781,919 842,981 748,964 765,1045 692,990 660,1068 628,990 555,1045 572,964 478,981 539,919 450,893 539,867 478,806 572,822 555,741 628,796"/>
    <text class="burst-small" x="660" y="872">and</text>
    <text class="burst-big" x="660" y="918">Moving</text>
    <text class="burst-small" x="660" y="952">More Copies</text>
  </svg>

  <h1 class="title-rest">That Sink Your<br>Indie-Released<br>Volume</h1>

  <p class="subtitle">A Newcomer's Manual for Releasing Solo, Arranging Pictures and Words, Planning Pages, Boosting Sign-ups</p>

  <p class="author">Dennis R. Walbrey</p>
  <p class="publisher">Quillmark Press</p>
</main>
</body>
</html>
```